Craft Beer Label / Barrel Aged

Our need: a label for a new beer. A beer aged in oak barrels. This label must respect certain codes: remind who the manufacturer is (Olvanq - see the site www.olvanq.fr) but also make visible the fact that the beer is aged in oak barrels.
This beer is a collaboration with the cellar of Sainte Ardelin. This collaboration must appear in graphic (logo) or textual form.
https://caveardelin.com/
the barrel used housed the following wine: https://boutique-caveardelin.com/produit/vernet-dubrac-blanc
This beer is rather premium, produced in small quantities, sold at wine merchants (specialty stores).
a text space (text not yet defined).
an ingredients area.
The imponderables: Brasseurs Autonomes logo, French flag, triman logo, pregnant woman logo, alcohol content (8.5% Alc. Vol. ), the volume 33 cl, the Terres du Midi logo, the bar code, the packer code EMB 47282K, the mention 'contains barley malt'.

Target Market(s)

30-40 years old / Clientele who enjoy craft beer / CSP+

Industry/Entity Type

Bière Artisanale / Agroalimentaire

Requirements
Must have
• see in the description the legal obligations that the label or back label must contain

```html
<!DOCTYPE html>
<html lang="en">
<head>
<meta charset="utf-8">
<title>Olvanq Barrel Aged – Label Set</title>
<link href="https://fonts.googleapis.com/css2?family=Fredoka:wght@500;600;700&family=Josefin+Sans:wght@600;700&display=swap" rel="stylesheet">
<style>
  :root {
    --paper: #fdf3ec;
    --label: #f7caa0;
    --label-deep: #f1a862;
    --ink: #2f3b35;
    --ribbon: #f3f2ee;
    --ornament: #f0b983;
  }
  html, body {
    margin: 0;
    width: 1200px;
    height: 799px;
    overflow: hidden;
    background: var(--paper);
  }
  .sheet { display: block; width: 1200px; height: 799px; }
  .outline { stroke: var(--ink); stroke-width: 2.2; stroke-linejoin: round; }
  .fill-label { fill: var(--label); }
  .fill-deep { fill: var(--label-deep); }
  .fill-ribbon { fill: var(--ribbon); }
  .ornament { fill: var(--ornament); }
  .title { font-family: "Fredoka", "Arial Rounded MT Bold", sans-serif; font-weight: 700; fill: var(--ink); text-anchor: middle; }
  .small { font-family: "Josefin Sans", Arial, sans-serif; font-weight: 700; fill: var(--ink); text-anchor: middle; letter-spacing: 1.5px; }
  .fine { font-family: "Josefin Sans", Arial, sans-serif; font-weight: 600; fill: var(--ink); text-anchor: middle; letter-spacing: 0.8px; }
  .number { font-family: "Fredoka", Arial, sans-serif; font-weight: 600; fill: var(--ink); text-anchor: middle; }
  .star { fill: var(--label); stroke: var(--ink); stroke-width: 1.5; stroke-linejoin: round; }
</style>
</head>
<body>
<svg class="sheet" viewBox="0 0 1060 706" preserveAspectRatio="none" xmlns="http://www.w3.org/2000/svg">
  <defs>
    <path id="craft-top-arc" d="M142,470 A78,78 0 0 1 298,470"/>
    <path id="craft-bottom-arc" d="M136,560 A84,84 0 0 0 304,560"/>
    <path id="badge-top-arc" d="M795,515 A60,60 0 0 1 915,515"/>
    <path id="badge-bottom-arc" d="M780,515 A75,75 0 0 0 930,515"/>
  </defs>

  <!-- Brand label: Olvanq barrel aged -->
  <g class="label label-brand">
    <path class="outline fill-deep" d="M218,52 C250,52 262,72 288,76 C310,80 318,100 312,122 C330,140 336,170 330,198 C340,228 326,258 312,268 C318,292 306,312 286,314 C262,318 250,336 218,336 C186,336 174,318 150,314 C130,312 118,292 124,268 C110,258 96,228 106,198 C100,170 106,140 124,122 C118,100 126,80 148,76 C174,72 186,52 218,52 Z"/>
    <path class="outline fill-label" d="M218,64 C246,64 256,82 280,86 C298,90 304,106 300,126 C316,144 322,170 316,198 C324,226 314,250 300,262 C304,284 296,300 278,304 C256,308 246,324 218,324 C190,324 180,308 158,304 C140,300 132,284 136,262 C122,250 112,226 120,198 C114,170 120,144 136,126 C132,106 138,90 156,86 C180,82 190,64 218,64 Z"/>
    <rect class="ornament" x="140" y="92" width="156" height="200" rx="70" role="img" aria-label="Scrolling filigree ornament"/>
    <ellipse class="outline fill-label" cx="218" cy="192" rx="78" ry="96"/>
    <ellipse class="outline fill-label" cx="218" cy="192" rx="70" ry="88"/>
    <text class="small" x="218" y="136" font-size="11">PREMIUM</text>
    <text class="small" x="218" y="156" font-size="11">QUALITY</text>
    <path class="outline fill-ribbon" d="M150,162 L286,162 L280,192 L286,222 L150,222 L156,192 Z"/>
    <text class="title" x="218" y="202" font-size="28">OLVANQ</text>
    <text class="small" x="218" y="236" font-size="11">BARREL</text>
    <text class="small" x="218" y="254" font-size="11">AGED</text>
  </g>

  <!-- Oak barrel label -->
  <g class="label label-oak-barrel">
    <path class="outline fill-deep" d="M452,92 C452,70 470,56 492,56 L568,56 C590,56 608,70 608,92 Z"/>
    <polygon class="star" points="480,68 483,75 490,75 484,79 486,86 480,82 474,86 476,79 470,75 477,75"/>
    <polygon class="star" points="502,64 505,71 512,71 506,75 508,82 502,78 496,82 498,75 492,71 499,71"/>
    <polygon class="star" points="530,60 534,69 543,69 536,74 539,83 530,78 521,83 524,74 517,69 526,69"/>
    <polygon class="star" points="558,64 561,71 568,71 562,75 564,82 558,78 552,82 554,75 548,71 555,71"/>
    <polygon class="star" points="580,68 583,75 590,75 584,79 586,86 580,82 574,86 576,79 570,75 577,75"/>
    <path class="outline fill-deep" d="M418,92 L642,92 L642,236 C642,290 600,318 530,330 C460,318 418,290 418,236 Z"/>
    <path class="outline fill-label" d="M428,100 L632,100 L632,236 C632,284 594,308 530,320 C466,308 428,284 428,236 Z"/>
    <rect class="ornament" x="450" y="250" width="160" height="56" rx="26" role="img" aria-label="Scrolling filigree ornament"/>
    <path class="outline fill-label" d="M402,118 C470,126 590,126 658,118 L650,170 L658,236 C590,244 470,244 402,236 L410,170 Z"/>
    <path class="outline fill-ribbon" d="M474,92 L586,92 L580,106 L586,120 L474,120 L480,106 Z"/>
    <text class="small" x="530" y="111" font-size="11">PREMIUM</text>
    <rect class="ornament" x="424" y="136" width="40" height="82" rx="18" role="img" aria-label="Barley ear illustration"/>
    <rect class="ornament" x="596" y="136" width="40" height="82" rx="18" role="img" aria-label="Barley ear illustration"/>
    <text class="title" x="530" y="168" font-size="36">OAK</text>
    <text class="title" x="530" y="210" font-size="36">BARREL</text>
    <path class="outline fill-ribbon" d="M464,234 C500,240 560,240 596,234 L590,252 L596,270 C560,264 500,264 464,270 L470,252 Z"/>
    <text class="small" x="530" y="258" font-size="10">SMALL BATCH</text>
    <circle class="outline fill-ribbon" cx="530" cy="310" r="20"/>
    <text class="number" x="530" y="315" font-size="12">33 cl</text>
  </g>

  <!-- Cask origin label -->
  <g class="label label-cask">
    <path class="outline fill-deep" d="M768,50 L940,50 L944,62 L962,66 L962,290 L944,296 L940,312 L890,312 C880,324 868,330 856,330 C844,330 832,324 822,312 L768,312 L764,296 L750,290 L750,66 L764,62 Z"/>
    <path class="outline fill-label" d="M774,58 L934,58 L938,70 L954,74 L954,284 L938,290 L934,304 L774,304 L770,290 L758,284 L758,74 L770,70 Z"/>
    <rect class="ornament" x="772" y="70" width="168" height="46" rx="20" role="img" aria-label="Scrolling filigree ornament"/>
    <rect class="ornament" x="772" y="208" width="168" height="26" rx="12" role="img" aria-label="Scrolling filigree ornament"/>
    <text class="title" x="856" y="148" font-size="38">BARREL</text>
    <text class="title" x="856" y="198" font-size="38">AGED</text>
    <path class="outline fill-ribbon" d="M738,232 L782,240 L782,266 Z"/>
    <path class="outline fill-ribbon" d="M974,232 L930,240 L930,266 Z"/>
    <path class="outline fill-ribbon" d="M782,240 C830,230 882,230 930,240 L930,266 C882,256 830,256 782,266 Z"/>
    <text class="small" x="856" y="257" font-size="10">WHITE WINE CASK</text>
    <text class="small" x="816" y="300" font-size="8">ALC.</text>
    <text class="small" x="898" y="300" font-size="8">VOL.</text>
    <circle class="outline fill-ribbon" cx="856" cy="294" r="18"/>
    <text class="number" x="856" y="299" font-size="13">8.5%</text>
  </g>

  <!-- Collaboration label -->
  <g class="label label-collab">
    <path class="outline fill-deep" d="M118,470 C118,408 164,362 220,362 C276,362 322,408 322,470 L322,570 C322,616 276,654 220,654 C164,654 118,616 118,570 Z"/>
    <path class="outline fill-label" d="M128,470 C128,414 170,372 220,372 C270,372 312,414 312,470 L312,570 C312,610 270,644 220,644 C170,644 128,610 128,570 Z"/>
    <text class="small" font-size="10"><textPath href="#craft-top-arc" startOffset="50%">OLVANQ × SAINTE ARDELIN</textPath></text>
    <circle class="ornament" cx="218" cy="446" r="30" role="img" aria-label="Hop cone illustration"/>
    <path class="outline fill-deep" d="M78,490 L122,490 L122,548 L78,548 L92,519 Z"/>
    <path class="outline fill-deep" d="M358,490 L314,490 L314,548 L358,548 L344,519 Z"/>
    <rect class="outline fill-deep" x="108" y="488" width="220" height="62"/>
    <text class="title" x="218" y="530" font-size="30">CRAFT BEER</text>
    <circle class="outline fill-ribbon" cx="218" cy="578" r="20"/>
    <text class="number" x="218" y="585" font-size="18">×</text>
    <text class="small" font-size="11"><textPath href="#craft-bottom-arc" startOffset="50%">AGED IN OAK BARRELS</textPath></text>
  </g>

  <!-- Ingredients label -->
  <g class="label label-ingredients">
    <path class="outline fill-deep" d="M412,378 L664,378 L664,580 C664,612 620,630 594,636 L538,652 L482,636 C456,630 412,612 412,580 Z"/>
    <path class="outline fill-label" d="M422,388 L654,388 L654,578 C654,604 616,620 592,626 L538,641 L484,626 C460,620 422,604 422,578 Z"/>
    <ellipse class="outline fill-deep" cx="538" cy="428" rx="44" ry="28"/>
    <circle class="ornament" cx="538" cy="428" r="18" role="img" aria-label="Hop cone illustration"/>
    <path class="outline fill-ribbon" d="M410,466 C430,466 440,458 446,454 L630,454 C636,458 646,466 666,466 C682,476 690,490 690,498 C690,506 682,520 666,530 C646,530 636,538 630,542 L446,542 C440,538 430,530 410,530 C394,520 386,506 386,498 C386,490 394,476 410,466 Z"/>
    <text class="title" x="538" y="511" font-size="34">INGREDIENTS</text>
    <path class="outline fill-deep" d="M450,536 L626,536 L618,562 L458,562 Z"/>
    <text class="small" x="538" y="553" font-size="9">CONTAINS BARLEY MALT</text>
    <text class="fine" x="538" y="584" font-size="10">WATER · BARLEY MALT · HOPS</text>
    <text class="fine" x="538" y="600" font-size="10">YEAST · OAK AGED</text>
    <text class="fine" x="538" y="618" font-size="8">EMB 47282K · 33 CL</text>
  </g>

  <!-- Round badge -->
  <g class="label label-badge">
    <path class="outline fill-deep" d="M855,368 C866,380 870,384 890,388 C930,396 990,440 990,515 C990,595 930,655 855,658 C780,655 720,595 720,515 C720,440 780,396 820,388 C840,384 844,380 855,368 Z"/>
    <path class="outline fill-label" d="M855,382 C864,392 872,396 890,400 C926,408 978,448 978,515 C978,588 924,644 855,646 C786,644 732,588 732,515 C732,448 784,408 820,400 C838,396 846,392 855,382 Z"/>
    <circle class="outline fill-label" cx="855" cy="515" r="108"/>
    <circle class="outline fill-deep" cx="855" cy="515" r="88"/>
    <circle class="outline fill-label" cx="855" cy="515" r="52"/>
    <text class="small" font-size="9"><textPath href="#badge-top-arc" startOffset="50%">PREMIUM QUALITY</textPath></text>
    <text class="small" font-size="9"><textPath href="#badge-bottom-arc" startOffset="50%">TERRES DU MIDI · 8.5% VOL.</textPath></text>
    <circle class="outline fill-ribbon" cx="855" cy="515" r="42"/>
    <text class="title" x="855" y="529" font-size="38">OA</text>
  </g>
</svg>
</body>
</html>
```